Plakate für Charity Unternehmen
Zielgruppe
Orno ist ein weltweit agierendes Charity Unternehmen.
Aufgabenstellung
Wir benötigen ein 'Plakat' Design, mit dem Zweck dieses Design als Banner, Sticker oder als Schild an unseren Projekten anzubringen. Das Schild soll in zwei verschiedenen Layouts geliefert werden.
1. Eine Art Blanko Version in der das Logo und das Motto eingearbeitet sind. Dieser Teil nimmt rund 1/3 des Plakats ein. Der Rest hat einen Freiraum auf dem wir Namen der Spender oder kooperative Charity Logos einsetzen können. Diese Version wird für Zusammenarbeit verwendet.
2. Eine zweite Version nimmt das gesamte Plakat ein, hier findet sich das Logo und das Motto welche das ganze Plakat einnehmen.
In beiden Fällen sollte die Aufteilung sauber und gut leserlich sein. Das Plakat wird in Auflösungen von bis zu 1,5m mal 1m gedruckt, sollte dementsprechend also die richtige Auflösung haben. Außerdem sollten Photoshop Datei möglichst mitgeliefert werden damit wir wenn nötig Namen und Logos einsetzen können.
Das einzuarbeitende Motto lautet:
إنما المؤمنون أخوة
Das Plakat sollte im Querformat sein und die Hintergrundfarbe sollte schwarz oder weiß sein.
Anbei befindet sich eine Beispieldatei wie das Plakat an den Projekten angebracht wird.

```html
<!DOCTYPE html>
<html lang="de">
<head>
<meta charset="utf-8">
<title>Orno – Plakat</title>
<link href="https://fonts.googleapis.com/css2?family=Noto+Naskh+Arabic:wght@700&family=Tinos&display=swap" rel="stylesheet">
<style>
  :root {
    --page: #e3e3e3;
    --paper: #fafafa;
    --stripe: #dcdde0;
    --stripe-soft: #ececee;
    --gold: #dcaf5c;
    --gold-deep: #c1924d;
    --ink: #111111;
    --white: #ffffff;
  }
  html, body {
    margin: 0;
    padding: 0;
    width: 1000px;
    height: 1200px;
    overflow: hidden;
    background: var(--page);
  }
  .canvas {
    position: relative;
    width: 1000px;
    height: 1200px;
  }
  .poster {
    position: absolute;
    left: 105px;
    width: 790px;
    background: var(--paper);
    overflow: hidden;
  }
  .poster--partner { top: 63px; height: 526px; }
  .poster--full { top: 610px; height: 533px; }
  .backdrop {
    position: absolute;
    inset: 0;
    width: 100%;
    height: 100%;
  }
  .brand {
    position: absolute;
    left: 0;
    right: 0;
    display: flex;
    flex-direction: column;
    align-items: center;
  }
  .brand__dot {
    border-radius: 50%;
    background: var(--gold);
  }
  .brand__name {
    font-family: "Tinos", "Times New Roman", serif;
    color: var(--ink);
    letter-spacing: 1px;
    line-height: 1;
  }
  .poster--partner .brand { top: 60px; }
  .poster--partner .brand__dot { width: 120px; height: 120px; margin-bottom: 44px; }
  .poster--partner .brand__name { font-size: 61px; }
  .poster--full .brand { top: 42px; }
  .poster--full .brand__dot { width: 100px; height: 100px; margin-bottom: 30px; }
  .poster--full .brand__name { font-size: 48px; }
  .rule {
    position: absolute;
    left: 0;
    right: 0;
    background: linear-gradient(var(--gold), var(--gold-deep));
  }
  .motto-band {
    position: absolute;
    left: 0;
    right: 0;
    display: flex;
    align-items: center;
    justify-content: center;
    background: linear-gradient(180deg, var(--gold) 0%, var(--gold) 40%, var(--gold-deep) 100%);
  }
  .motto {
    margin: 0;
    font-family: "Noto Naskh Arabic", serif;
    font-weight: 700;
    color: var(--white);
    font-size: 66px;
    line-height: 1;
    padding-top: 8px;
    direction: rtl;
  }
</style>
</head>
<body>
<div class="canvas">

  <!-- Partner version: logo and motto in the upper third, open space below -->
  <section class="poster poster--partner">
    <svg class="backdrop" viewBox="0 0 790 526" preserveAspectRatio="none" aria-hidden="true">
      <polygon points="0,160 0,270 790,-74 790,-184" fill="var(--stripe-soft)"/>
      <polygon points="0,270 0,360 790,16 790,-74" fill="var(--white)"/>
      <polygon points="0,333 0,400 790,56 790,30" fill="var(--stripe)" opacity="0.7"/>
      <polygon points="0,420 0,526 150,526 790,247 790,132" fill="var(--stripe-soft)"/>
      <polygon points="0,470 0,526 790,526 790,282" fill="var(--white)" opacity="0.6"/>
      <polygon points="250,526 505,526 790,402 790,290" fill="var(--white)"/>
      <polygon points="770,526 790,526 790,517" fill="var(--white)"/>
    </svg>
    <div class="brand">
      <span class="brand__dot"></span>
      <span class="brand__name">ORNO</span>
    </div>
    <div class="rule" style="top:310px;height:4px"></div>
    <div class="motto-band" style="top:320px;height:122px">
      <p class="motto" lang="ar">إنما المؤمنون أخوة</p>
    </div>
    <div class="rule" style="top:450px;height:9px"></div>
  </section>

  <!-- Full version: logo and motto across the whole poster -->
  <section class="poster poster--full">
    <svg class="backdrop" viewBox="0 0 790 533" preserveAspectRatio="none" aria-hidden="true">
      <polygon points="0,100 0,160 790,-184 790,-124" fill="var(--stripe-soft)"/>
      <polygon points="0,170 0,240 790,-104 790,30" fill="var(--stripe-soft)" opacity="0.8"/>
      <polygon points="0,245 0,330 790,-14 790,60" fill="var(--white)"/>
      <polygon points="0,345 0,430 790,86 790,30" fill="var(--stripe)" opacity="0.45"/>
      <polygon points="0,430 0,520 790,176 790,100" fill="var(--stripe-soft)"/>
      <polygon points="180,520 420,520 790,360 790,250" fill="var(--white)"/>
      <polygon points="0,310 0,350 60,324" fill="var(--stripe)" opacity="0.7"/>
    </svg>
    <div class="brand">
      <span class="brand__dot"></span>
      <span class="brand__name">ORNO</span>
    </div>
    <div class="motto-band" style="top:243px;height:104px">
      <p class="motto" lang="ar">إنما المؤمنون أخوة</p>
    </div>
    <div class="rule" style="top:513px;height:20px"></div>
  </section>

</div>
</body>
</html>
```